Business card design needed

Our modern electrical contracting company requires business card design utilising our logo and incorporating our tag line "Service when you need it". We specialise in assisting our customers 24/7 offering a breakdown service.

Industry/Entity Type

Electrical

Contact Information for Business Card

Marcus Penhale, Electrical contractor,Tel: (08) 8456 3071, Fax: (08) 8679 4315, Mob 0438 562 740, Email: marcus.penhale@brightwirepower.com.au, Web: www.brightwirepower.com.au

Requirements
Must have
• we require a 2 sided card.
Front- Logo, tag line and contact information.
Rear- service when you need it! Call now for our 24/7 breakdown service

```html
<!DOCTYPE html>
<html lang="en">
<head>
<meta charset="utf-8">
<title>Brightwire Power – Business Card</title>
<link rel="stylesheet" href="https://fonts.googleapis.com/css2?family=Source+Sans+3:ital,wght@0,400;0,600;0,700;1,400&display=swap">
<style>
  :root {
    --page-bg: #cfcfcf;
    --card-white: #f4f4f4;
    --card-silver: #c9c9c9;
    --ink: #1e1e1e;
    --ink-heading: #2f2b2b;
    --accent-blue: #1f6fb0;
    --brand-blue: #2b4a9c;
    --band-dark: #2a2626;
    --rear-dark: #2a2727;
    --flap-white: #ececec;
    --rule-light: #d9d9d9;
  }
  * { box-sizing: border-box; margin: 0; padding: 0; }
  html, body {
    width: 1200px; height: 1000px; overflow: hidden;
    background: var(--page-bg);
    font-family: "Source Sans 3", "Myriad Pro", sans-serif;
  }
  .canvas { position: relative; width: 1200px; height: 1000px; }

  /* ---------- Front ---------- */
  .card-front {
    position: absolute; left: 235px; top: 15px; width: 738px; height: 444px;
    background: linear-gradient(150deg, var(--card-white) 0%, #f2f2f2 55%, var(--card-silver) 100%);
    overflow: hidden;
  }
  .brand-lockup {
    position: absolute; display: flex; align-items: center; gap: 8px;
    font-weight: 700; color: var(--brand-blue); white-space: nowrap;
  }
  .brand-lockup .brand-dot { border-radius: 50%; background: var(--brand-blue); flex: none; }
  .front-header-brand { left: 22px; top: 80px; width: 153px; height: 64px; background: #fff; justify-content: center; font-size: 16px; gap: 6px; }
  .front-header-brand .brand-dot { width: 14px; height: 14px; }
  .header-divider { position: absolute; left: 202px; top: 80px; width: 2px; height: 65px; background: var(--ink-heading); }
  .tagline-main { position: absolute; left: 220px; top: 74px; font-size: 47px; font-weight: 700; color: var(--ink-heading); letter-spacing: -0.5px; line-height: 1; }
  .tagline-sub { position: absolute; left: 284px; top: 126px; font-size: 13.5px; font-weight: 700; color: var(--ink); }

  .contact-name { position: absolute; left: 43px; top: 231px; font-size: 21px; color: var(--ink); white-space: nowrap; }
  .contact-name strong { color: var(--accent-blue); font-weight: 600; }
  .contact-name span { font-size: 17px; }
  .rule { position: absolute; height: 1.5px; background: var(--ink); }
  .rule-top { left: 43px; top: 271px; width: 392px; }
  .rule-bottom { left: 40px; top: 334px; width: 391px; }
  .contact-line { position: absolute; font-size: 15.5px; color: var(--ink); white-space: nowrap; }
  .contact-line .label { color: var(--accent-blue); }
  .contact-phones { left: 45px; top: 276px; }
  .contact-email { left: 51px; top: 311px; }
  .contact-web { left: 47px; top: 355px; font-size: 16px; }
  .contact-web strong { color: var(--accent-blue); font-weight: 600; font-size: 18px; }

  .front-band { position: absolute; left: 0; top: 408px; width: 738px; height: 36px; }
  .front-corner-brand { right: 8px; top: 380px; font-size: 19px; flex-direction: column; gap: 6px; }
  .front-corner-brand .brand-dot { width: 40px; height: 40px; }

  /* ---------- Rear ---------- */
  .card-rear {
    position: absolute; left: 225px; top: 482px; width: 779px; height: 466px;
    background: var(--rear-dark); overflow: hidden; color: #fff;
  }
  .rear-flaps { position: absolute; inset: 0; }
  .rear-brand { left: 62px; top: 176px; width: 324px; flex-direction: column; gap: 22px; font-size: 30px; letter-spacing: 0.5px; }
  .rear-brand .brand-dot { width: 84px; height: 84px; }
  .rear-divider { position: absolute; left: 398px; top: 165px; width: 2px; height: 141px; background: var(--rule-light); }
  .rear-tagline { position: absolute; left: 420px; top: 227px; font-size: 18px; font-weight: 600; }
  .rear-call { position: absolute; left: 0; width: 100%; top: 374px; text-align: center; font-size: 22px; font-style: italic; }
</style>
</head>
<body>
<main class="canvas">

  <section class="card-front" aria-label="Card front">
    <div class="brand-lockup front-header-brand"><span class="brand-dot"></span>BRIGHTWIRE POWER</div>
    <div class="header-divider"></div>
    <p class="tagline-main">Service</p>
    <p class="tagline-sub">when you need it</p>

    <p class="contact-name"><strong>Marcus Penhale</strong><span>| Electrical Contractor</span></p>
    <div class="rule rule-top"></div>
    <p class="contact-line contact-phones"><span class="label">Tel:</span> (08) 8456 3071 <span class="label">Fax:</span> (08) 8679 4315 <span class="label">Mob:</span> 0438 562 740</p>
    <p class="contact-line contact-email"><span class="label">E-mail:</span> marcus.penhale@brightwirepower.com.au</p>
    <div class="rule rule-bottom"></div>
    <p class="contact-line contact-web">www.<strong>brightwirepower</strong>.com.au</p>

    <svg class="front-band" viewBox="0 0 738 36" aria-hidden="true">
      <defs>
        <linearGradient id="bandShade" x1="0" y1="0" x2="0" y2="1">
          <stop offset="0" stop-color="#3a3535"/>
          <stop offset="1" stop-color="#1f1c1c"/>
        </linearGradient>
      </defs>
      <polygon points="0,0 496,0 516,36 0,36" fill="url(#bandShade)"/>
    </svg>
    <div class="brand-lockup front-corner-brand"><span class="brand-dot"></span>BRIGHTWIRE POWER</div>
  </section>

  <section class="card-rear" aria-label="Card back">
    <svg class="rear-flaps" viewBox="0 0 779 466" aria-hidden="true">
      <polygon points="0,40 39,63 39,433 0,454" fill="var(--flap-white)"/>
      <polygon points="779,40 741,63 741,433 779,454" fill="var(--flap-white)"/>
    </svg>
    <div class="brand-lockup rear-brand"><span class="brand-dot"></span>BRIGHTWIRE POWER</div>
    <div class="rear-divider"></div>
    <p class="rear-tagline">service when you need it</p>
    <p class="rear-call">Call now for our 24/7 breakdown service</p>
  </section>

</main>
</body>
</html>
```